Project business card design for VORELDA

We need a card business design for our brand VORELDA. VORELDA is the brand for a special aluminium window. It is like the typical Sorrento design but stronger. It has a modern design and includes a new patented opening system. Fee free to look at the webpage for more information.

Enclosed logo.

On one side of the card should be the logo only and in the other the information provided and the logo on a smaller scale.

The card should have a clean design. Easy to read.
Updates

Sorry I forget to include my name on the card: Ángel L. MoralesGerente General Added Monday, December 02, 2013

Target Market(s)

Constructors, arquitects, designers...

Contact Information for Business Card

Tomas R. Quintero
Gerente General

Valdrina Costera, srl.
Pedro J. Alcaraz #48 Apto. 204
Jardines Velarde. Santo Domingo
Republica Dominicana.
Tel.: 849 375 4162
E-mail: info@vorelda.eu
www.vorelda.eu

Requirements
Must have
• must have only the logo on one side of the card on a larger scale.
Nice to have
• The card should have a clean design. Easy to read.

```html
<!DOCTYPE html>
<html lang="es">
<head>
<meta charset="utf-8">
<title>VORELDA – business card sheet</title>
<link rel="stylesheet" href="https://fonts.googleapis.com/css2?family=Arimo:wght@400&display=swap">
<style>
  :root {
    --paper: #ffffff;
    --ink: #1a1a1a;
    --mark: #111111;
    --brand-blue: #1f6fb8;
    --brand-sky: #2b9be0;
    --brand-green: #6cb33f;
  }
  html, body {
    margin: 0;
    padding: 0;
    width: 1200px;
    height: 925px;
    overflow: hidden;
    background: var(--paper);
  }
  .sheet {
    position: relative;
    width: 1200px;
    height: 925px;
    font-family: "Arimo", Arial, Helvetica, sans-serif;
    color: var(--ink);
  }
  .crop-marks {
    position: absolute;
    inset: 0;
    width: 1200px;
    height: 925px;
  }
  .crop-marks line {
    stroke: var(--mark);
    stroke-width: 0.6;
  }
  .brand {
    position: absolute;
    display: flex;
    flex-direction: column;
    align-items: center;
    justify-content: center;
    font-weight: 400;
    letter-spacing: 1px;
    color: var(--brand-blue);
  }
  .brand-square {
    display: block;
    flex: none;
    background: linear-gradient(180deg, var(--brand-sky), var(--brand-green));
  }
  /* logo-only front side */
  .brand--front {
    left: 77px;
    top: 91px;
    width: 513px;
    height: 281px;
    gap: 16px;
    font-size: 44px;
    letter-spacing: 3px;
  }
  .brand--front .brand-square {
    width: 150px;
    height: 150px;
  }
  /* small logo on the info side */
  .brand--back {
    left: 657px;
    top: 537px;
    width: 130px;
    height: 240px;
    gap: 8px;
    font-size: 24px;
  }
  .brand--back .brand-square {
    width: 70px;
    height: 70px;
  }
  .contact {
    position: absolute;
    left: 810px;
    top: 548px;
    margin: 0;
    font-size: 17px;
    line-height: 20.5px;
    font-style: normal;
  }
  .contact span { display: block; }
  .contact .contact-role { margin-bottom: 10px; }
</style>
</head>
<body>
<main class="sheet">
  <svg class="crop-marks" viewBox="0 0 590 455" preserveAspectRatio="none" aria-hidden="true">
    <line x1="38" y1="0" x2="38" y2="18"/>
    <line x1="0" y1="45" x2="25" y2="45"/>
    <line x1="0" y1="183" x2="25" y2="183"/>
    <line x1="38" y1="190" x2="38" y2="218"/>
    <line x1="290" y1="0" x2="290" y2="28"/>
    <line x1="312" y1="37" x2="336" y2="37"/>
    <line x1="312" y1="183" x2="336" y2="183"/>
    <line x1="290" y1="195" x2="290" y2="246"/>
    <line x1="245" y1="253" x2="268" y2="253"/>
    <line x1="245" y1="397" x2="268" y2="397"/>
    <line x1="290" y1="425" x2="290" y2="455"/>
    <line x1="541" y1="215" x2="541" y2="243"/>
    <line x1="565" y1="253" x2="590" y2="253"/>
    <line x1="555" y1="397" x2="580" y2="397"/>
    <line x1="541" y1="410" x2="541" y2="438"/>
  </svg>

  <div class="brand brand--front">
    <span class="brand-square"></span>
    <span class="brand-name">VORELDA</span>
  </div>

  <div class="brand brand--back">
    <span class="brand-square"></span>
    <span class="brand-name">VORELDA</span>
  </div>
  <address class="contact">
    <span class="contact-name">Tomás R. Quintero</span>
    <span class="contact-role">Gerente General</span>
    <span>Valdrina Costera, srl.</span>
    <span>Av. Duarte Peralta,</span>
    <span>No.1740. Plaza Oria,</span>
    <span>Suite 5. Jardines Velarde,</span>
    <span>Santo Domingo</span>
    <span>República Dominicana</span>
    <span>Tel.: 849 375 4162</span>
    <span>E-mail: info@vorelda.eu</span>
    <span>www.vorelda.eu</span>
  </address>
</main>
</body>
</html>
```